Front & Back cover design for timber flooring brochure - A4 size

I need a design for the front and back cover of an A4 sized brochure for a timber and concrete flooring company called "Grand Oak Surfaces". The front cover should include the logo (attached), and an image + tagline for each of the three products/services that they offer which are:

1. Timber Flooring
2. Concrete Grinding & Sealing
3. Floor sanding (i have attached a photo for each of these three - however feel free to use other images if you feel they are better).

The back cover should be simple, perhaps just a continuation of the colour or graphic scheme on the front with the company contact details at the bottom.

Industry/Entity Type

Flooring

Requirements
Must have
• front cover has to have the logo with an image and text of the 3 services described. You can use the images attached or your own.

```html
<!DOCTYPE html>
<html lang="en">
<head>
<meta charset="utf-8">
<title>Grand Oak Surfaces – Brochure Cover</title>
<link rel="stylesheet" href="https://fonts.googleapis.com/css2?family=Cinzel:wght@600&family=Open+Sans:ital,wght@0,700;1,600;1,700&display=swap">
<style>
  :root {
    --bg: #131417;
    --label-ink: #1a1208;
    --contact-cream: #f3e7a8;
    --tagline-cream: #f1e8cc;
    --bullet: #c7652c;
    --band-dark: #3d2306;
    --band-gold: #b8953e;
    --band-light: #efe2b4;
    --band-rust: #7b3a18;
    --band-wine: #4f150d;
  }
  * { margin: 0; padding: 0; box-sizing: border-box; }
  html, body { width: 1200px; height: 842px; overflow: hidden; background: var(--bg); }
  .cover { position: relative; width: 1200px; height: 842px; background: var(--bg); overflow: hidden; }

  .metal-band {
    position: absolute; left: 0; width: 1200px;
    background: linear-gradient(90deg, var(--band-dark) 0%, var(--band-gold) 25%, var(--band-light) 60%, var(--band-rust) 85%, var(--band-wine) 100%);
  }
  .metal-band--top { top: 0; height: 12px; }
  .metal-band--bottom { top: 795px; height: 47px; }

  .brand-name {
    font-family: "Open Sans", sans-serif; font-style: normal; font-weight: 700;
    color: var(--tagline-cream); text-transform: uppercase; white-space: nowrap;
    text-align: center; position: absolute;
  }

  /* Back cover */
  .back-cover { position: absolute; left: 0; top: 0; width: 600px; height: 842px; }
  .back-cover .brand-name {
    left: 0; top: 592px; width: 600px; font-size: 26px; letter-spacing: 2px;
  }
  .contact {
    position: absolute; left: 0; width: 600px; text-align: center;
    font-family: "Open Sans", sans-serif; font-style: italic; font-weight: 600;
    color: var(--contact-cream);
  }
  .contact--address { top: 660px; font-size: 15px; line-height: 17px; }
  .contact--lines { top: 733px; font-size: 13px; line-height: 18px; }
  .contact--lines span + span { margin-left: 10px; }

  /* Front cover */
  .service-panel { position: absolute; left: 630px; width: 539px; height: 156px; }
  .service-panel--timber { top: 53px; background: linear-gradient(160deg, #8c2f0a 0%, #c5521c 40%, #d8733a 70%, #b0461a 100%); }
  .service-panel--concrete { top: 223px; background: linear-gradient(180deg, #6d7d68 0%, #8a9a85 45%, #a0ae98 60%, #7d8c74 100%); }
  .service-panel--sanding { top: 393px; background: linear-gradient(180deg, #b8541c 0%, #d9803e 45%, #c96a2c 70%, #a9481a 100%); }
  .service-label {
    position: absolute; left: 3px; bottom: -3px;
    font-family: "Cinzel", serif; font-weight: 600; color: var(--label-ink);
    font-size: 27px; letter-spacing: 1.5px; line-height: 1;
  }

  .front-cover .brand-name {
    left: 630px; top: 624px; width: 539px; font-size: 38px; letter-spacing: 2px;
  }

  .service-tagline {
    position: absolute; left: 630px; top: 744px; width: 545px;
    display: flex; justify-content: space-between; align-items: center;
    font-family: "Open Sans", sans-serif; font-style: italic; font-weight: 700;
    font-size: 18px; color: var(--tagline-cream); white-space: nowrap;
  }
  .service-tagline li { list-style: none; display: flex; align-items: center; }
  .service-tagline li::before {
    content: ""; width: 9px; height: 9px; background: var(--bullet); margin-right: 2px;
  }
</style>
</head>
<body>
<main class="cover">
  <div class="metal-band metal-band--top"></div>

  <section class="back-cover">
    <div class="brand-name">Grand Oak Surfaces</div>
    <address class="contact contact--address">
      42 Millbrook Yard,<br>Ashford Vale,<br>Westshire,<br>WV12 4QT
    </address>
    <div class="contact contact--lines">
      <div><span>Tel: 01632 960 418</span><span>Fax: 01632 960 419</span></div>
      <div><span>Email: hello@grandoaksurfaces.co.uk</span><span>Web: www.grandoaksurfaces.co.uk</span></div>
    </div>
  </section>

  <section class="front-cover">
    <div class="service-panel service-panel--timber" role="img" aria-label="Close-up photo of polished reddish timber floorboards">
      <h2 class="service-label">Timber Flooring</h2>
    </div>
    <div class="service-panel service-panel--concrete" role="img" aria-label="Photo of a glossy ground and sealed concrete floor">
      <h2 class="service-label">Concrete Grinding &amp; Sealing</h2>
    </div>
    <div class="service-panel service-panel--sanding" role="img" aria-label="Photo of freshly sanded pine board with a knot">
      <h2 class="service-label">Floor sanding</h2>
    </div>

    <div class="brand-name">Grand Oak Surfaces</div>

    <ul class="service-tagline">
      <li>Timber Flooring</li>
      <li>Concrete Grinding &amp; Sealing</li>
      <li>Floor sanding</li>
    </ul>
  </section>

  <div class="metal-band metal-band--bottom"></div>
</main>
</body>
</html>
```